Business Card Design Project

I require a business card with the following information on them for various different people;
name
m:
f:
e:
I have a logo already and will attached that. We are in the construction industry. I require something clean and simple but eye catching at the same time. You can use another colour with our logo if you like and you can style the logo as well if you wish. I am open.
Also it needs to be front and back design.
Industry/Entity Type
Construction
Requirements
Must have
- Logo, name, mobile, fax and email address.
Front and back design

```html
<!DOCTYPE html>
<html lang="en">
<head>
<meta charset="utf-8">
<title>Stonebridge Builds — Business Cards</title>
<link rel="stylesheet" href="https://fonts.googleapis.com/css2?family=Questrial&family=Open+Sans:wght@400;600&display=swap">
<style>
  :root {
    --bg: #e4e5e7;
    --card-dark: #1a1717;
    --card-light: #ffffff;
    --green: #5bb531;
    --ink: #1d1d1d;
    --ink-soft: #333333;
    --white: #ffffff;
  }
  * { margin: 0; padding: 0; box-sizing: border-box; }
  html, body { width: 1200px; height: 944px; overflow: hidden; background: var(--bg); }
  .canvas { position: relative; width: 1200px; height: 944px; }

  .card {
    position: absolute;
    width: 620px;
    height: 360px;
    border-radius: 22px;
    overflow: hidden;
    box-shadow: 0 10px 26px rgba(0,0,0,0.22);
  }

  .brand {
    display: flex;
    align-items: center;
    gap: 14px;
    font-family: "Questrial", sans-serif;
    color: var(--green);
    white-space: nowrap;
  }
  .brand-mark { background: var(--green); flex: none; }

  /* Back */
  .card-back { left: 70px; top: 80px; background: var(--card-dark); }
  .card-back .brand {
    position: absolute; left: 0; right: 0; top: 120px;
    justify-content: center; font-size: 50px;
  }
  .card-back .brand-mark { width: 38px; height: 38px; }
  .card-back .website {
    position: absolute; left: 0; right: 0; top: 232px;
    text-align: center;
    font-family: "Open Sans", sans-serif; font-weight: 600;
    font-size: 19px; letter-spacing: 1.5px; color: var(--white);
  }

  /* Front */
  .card-front { left: 510px; top: 494px; background: var(--card-light); }
  .card-front .swoosh { position: absolute; inset: 0; }
  .card-front .brand {
    position: absolute; left: 150px; top: 70px; font-size: 40px;
  }
  .card-front .brand-mark { width: 30px; height: 30px; }

  .person { position: absolute; left: 58px; top: 168px; font-family: "Open Sans", sans-serif; }
  .person-name { font-size: 24px; font-weight: 600; color: var(--ink); }
  .person-role { font-size: 16px; color: var(--green); margin-top: 2px; }

  .contact { position: absolute; font-family: "Open Sans", sans-serif; font-size: 16px; color: var(--ink-soft); list-style: none; white-space: nowrap; }
  .contact li { display: flex; align-items: center; gap: 9px; line-height: 23px; }
  .contact svg { width: 15px; height: 15px; flex: none; }
  .contact-phone { left: 58px; top: 262px; }
  .contact-online { left: 296px; top: 272px; }
  .contact-online .web { font-weight: 600; color: var(--ink); }
</style>
</head>
<body>
<main class="canvas">

  <section class="card card-back" aria-label="Card back">
    <div class="brand"><span class="brand-mark"></span>Stonebridge Builds</div>
    <p class="website">www.stonebridgebuilds.com</p>
  </section>

  <section class="card card-front" aria-label="Card front">
    <svg class="swoosh" viewBox="0 0 620 360" preserveAspectRatio="none" aria-hidden="true">
      <path d="M0,0 H150 Q50,30 0,170 Z" fill="var(--green)"/>
      <path d="M158,0 Q40,40 0,190" fill="none" stroke="var(--ink)" stroke-width="6"/>
      <path d="M620,360 H545 Q610,330 620,225 Z" fill="var(--green)"/>
      <path d="M520,360 Q605,320 620,200" fill="none" stroke="var(--ink)" stroke-width="5"/>
    </svg>

    <div class="brand"><span class="brand-mark"></span>Stonebridge Builds</div>

    <div class="person">
      <p class="person-name">Mark Ellison</p>
      <p class="person-role">director</p>
    </div>

    <ul class="contact contact-phone">
      <li>
        <svg viewBox="0 0 16 16" aria-hidden="true"><path d="M4 1 L6.5 4.5 L5 6.5 Q6.5 9.5 9.5 11 L11.5 9.5 L15 12 L13 15 Q4 14 1 3 Z" fill="var(--green)"/></svg>
        555-014-2200
      </li>
      <li>
        <svg viewBox="0 0 16 16" aria-hidden="true"><rect x="1" y="7" width="14" height="7" rx="1" fill="var(--green)"/><rect x="4" y="2" width="8" height="5" fill="none" stroke="var(--green)" stroke-width="1.5"/></svg>
        555-014-2201
      </li>
    </ul>

    <ul class="contact contact-online">
      <li>
        <svg viewBox="0 0 16 16" aria-hidden="true"><rect x="1" y="3" width="14" height="10" rx="1" fill="var(--green)"/><path d="M1.5 3.5 L8 9 L14.5 3.5" fill="none" stroke="var(--white)" stroke-width="1.3"/></svg>
        info@stonebridgebuilds.com
      </li>
      <li class="web">
        <svg viewBox="0 0 16 16" aria-hidden="true"><circle cx="8" cy="8" r="7" fill="var(--green)"/></svg>
        www.stonebridgebuilds.com
      </li>
    </ul>
  </section>

</main>
</body>
</html>
```